professional business card

Professional business card with logo on one side, and underneath logo list:
- power
-data
-fibre optic
-isolar

On other side:
Marcus Webb
Owner
MOB 0432 958 720
marcus@vorn.com.au
www.vornelectrical.com.au

Please edit logo to just leave VORN

```html
<!DOCTYPE html>
<html lang="en">
<head>
<meta charset="utf-8">
<title>VORN Electrical – Business Card</title>
<link rel="stylesheet" href="https://fonts.googleapis.com/css2?family=Barlow:wght@500;600;700&display=swap">
<style>
  :root {
    --teal: #1a9fa3;
    --grey: #7a7a7a;
    --paper: #ffffff;
    --page: #ffffff;
  }
  * { margin: 0; padding: 0; box-sizing: border-box; }
  html, body {
    width: 1200px;
    height: 1200px;
    overflow: hidden;
    background: var(--page);
    font-family: "Barlow", Arial, sans-serif;
  }
  .canvas { position: relative; width: 1200px; height: 1200px; }

  .card {
    position: absolute;
    left: 230px;
    width: 740px;
    height: 423px;
    background: var(--paper);
    box-shadow: 3px 5px 8px rgba(0, 0, 0, 0.22);
  }
  .card--front { top: 118px; }
  .card--back  { top: 659px; }

  .card__line {
    position: absolute;
    line-height: 1;
    white-space: nowrap;
  }
  .card--front .card__line {
    left: 0;
    width: 100%;
    text-align: center;
  }

  .brand-name {
    top: 108px;
    font-size: 120px;
    font-weight: 600;
    color: var(--teal);
    letter-spacing: 2px;
  }
  .services {
    top: 318px;
    font-size: 34px;
    font-weight: 600;
    color: var(--grey);
    letter-spacing: 4px;
  }
  .services__dot { margin: 0 2px; }

  .card--back .card__line {
    left: 89px;
    font-size: 34px;
    font-weight: 600;
    color: var(--grey);
    letter-spacing: 2.5px;
  }
  .card--back .contact-name {
    top: 74px;
    font-size: 34px;
    font-weight: 700;
    color: var(--teal);
  }
  .contact-role   { top: 113px; }
  .contact-mobile { top: 190px; }
  .contact-email  { top: 228px; }
  .contact-web    { top: 305px; }
</style>
</head>
<body>
  <main class="canvas">
    <section class="card card--front" aria-label="Card front">
      <div class="card__line brand-name">VORN</div>
      <div class="card__line services">POWER<span class="services__dot">·</span>DATA<span class="services__dot">·</span>FIBRE OPTIC<span class="services__dot">·</span>ISOLAR</div>
    </section>

    <section class="card card--back" aria-label="Card back">
      <div class="card__line contact-name">MARCUS WEBB</div>
      <div class="card__line contact-role">OWNER</div>
      <div class="card__line contact-mobile">MOB 0432 958 720</div>
      <div class="card__line contact-email">MARCUS@VORN.COM.AU</div>
      <div class="card__line contact-web">WWW.VORNELECTRICAL.COM.AU</div>
    </section>
  </main>
</body>
</html>
```